The Corvane Agency

We are a pr, social media and strategy agency specializing in the pet industry. We would like a new dynamic design of our existing website. We think it is currently outdated and looks too corporate. We would like it to look more consumer oriented as we primarily market pet products. We would like warm imagery involving pets and while pets are fun, this is still a business website and needs to maintain a professional look. We are hired by business owners and executives.
I would like some of our work featured on the home page.
Our primary service tabs are:
Public Relations
Social Media
Product Consulting
Most of the content will remain the same but we are open to suggestions!
Our current website can be found at www.lorvishdogpr.com.
We are open to other colors than in our logo and on our current page.
This is a design only project and will not require programming. The selected designer will need to provide at least one interior page in addition to the home page.

Industry/Entity Type

Pet

Requirements
Should not have
• Cartoon type figures. Pet puns.

```html
<!DOCTYPE html>
<html lang="en">
<head>
<meta charset="utf-8">
<title>The Corvane Agency</title>
<link href="https://fonts.googleapis.com/css2?family=Oswald:wght@400;500&family=Roboto:ital,wght@0,300;0,400;1,300&display=swap" rel="stylesheet">
<style>
:root{
  --red:#e31b23;
  --ink:#222;
  --text:#666;
  --nav:#111;
  --panel:#f5f5f5;
  --line:#e2e2e2;
  --orange:#e8a53c;
  --orange-dark:#b8771e;
  --rust:#e0601f;
  --rust-dark:#a8400f;
  --green:#4e8b2c;
  --green-dark:#31621a;
}
*{box-sizing:border-box;margin:0;padding:0}
html,body{width:900px;height:1200px;overflow:hidden;background:#fff}
body{font-family:"Roboto",Arial,sans-serif;color:var(--text);position:relative}
.wrap{position:absolute;left:98px;width:704px}

.brand{position:absolute;left:98px;top:20px;font-weight:400;font-size:24px;line-height:1;color:var(--red);letter-spacing:-.5px;display:flex;align-items:center;gap:6px}
.brand-dot{width:7px;height:7px;border-radius:50%;background:var(--red)}
.top-links{position:absolute;right:98px;top:12px;font-size:9.5px;color:#555;letter-spacing:.3px}
.top-links span{margin:0 4px;color:#999}
.search{position:absolute;right:98px;top:36px;width:165px;height:23px;background:#f1f1f1;border:1px solid #ddd;border-radius:2px}
.search svg{position:absolute;right:5px;top:3px}

.hero{position:absolute;left:0;top:92px;width:900px;height:443px;
  background:linear-gradient(100deg,#4f7d2c 0%,#8aa857 14%,#d2a78a 30%,#3c3431 46%,#4a3e38 56%,#e0b99c 72%,#9ab36a 88%,#5e8b34 100%)}
.nav{position:absolute;left:98px;top:70px;width:704px;height:35px;background:var(--nav);display:flex;align-items:center;font-family:"Oswald",Arial,sans-serif;font-size:13.5px;color:#fff;text-transform:uppercase;z-index:2}
.nav a{color:#fff;text-decoration:none;height:100%;display:flex;align-items:center}
.nav .active{background:var(--red);padding:0 16px}
.nav-items{flex:1;height:100%;display:flex;justify-content:space-between;padding:0 13px 0 17px}
.caption{position:absolute;left:98px;top:315px;width:712px;height:70px;background:rgba(90,90,90,.6);display:flex;align-items:center;justify-content:center;font-family:"Oswald",Arial,sans-serif;font-size:50px;color:#fff;text-shadow:1px 2px 3px rgba(0,0,0,.5)}
.arrow{position:absolute;top:20px;width:28px;height:28px;border-radius:50%;background:#eee;display:flex;align-items:center;justify-content:center}
.arrow.prev{left:6px}.arrow.next{right:6px}

.service{position:absolute;top:423px;height:134px;padding-top:4px;text-align:center;font-family:"Oswald",Arial,sans-serif;font-size:20px;color:#fff;text-shadow:1px 1px 2px rgba(0,0,0,.3)}
.service .thumb{position:absolute;left:9px;right:9px;top:32px;height:96px;border:1px solid #fff}
.service .foot{position:absolute;left:-4px;right:-4px;bottom:-1px;height:6px;clip-path:polygon(0 100%,4px 0,calc(100% - 4px) 0,100% 100%)}
.svc-pr{left:98px;width:224px;background:var(--orange)}
.svc-pr .foot{background:var(--orange-dark)}
.svc-pr .thumb{background:linear-gradient(120deg,#d9b46a,#f1ece2 50%,#8aa656)}
.svc-sm{left:338px;width:225px;background:var(--rust)}
.svc-sm .foot{background:var(--rust-dark)}
.svc-sm .thumb{background:linear-gradient(110deg,#3b5a9a,#c8b9a6 45%,#4a3322)}
.svc-pc{left:576px;width:225px;background:var(--green)}
.svc-pc .foot{background:var(--green-dark)}
.svc-pc .thumb{background:linear-gradient(110deg,#2b2f3a,#e4dfd9 45%,#b08a70)}

.section-title{font-family:"Oswald",Arial,sans-serif;font-weight:400;font-size:21px;color:var(--ink)}
.section-title em{font-style:normal;color:var(--red)}
.about{top:610px;text-align:center}
.about p{margin-top:10px;font-size:10px;font-weight:300;line-height:17.5px;color:#666}
.divider{position:absolute;left:0;width:900px;height:10px;background:linear-gradient(#f0f0f0,#fff)}

.card{position:absolute;top:735px;height:166px;background:var(--panel);border:1px solid var(--line);padding:10px 10px 10px 15px}
.team{left:98px;width:345px}
.team p{margin-top:8px;font-size:10px;font-weight:300;line-height:17.4px;color:#555;hyphens:auto}
.team .more{margin-top:5px;font-family:"Oswald",Arial,sans-serif;font-size:13px;color:var(--ink)}
.blog{left:458px;width:344px}
.dots{display:flex;gap:5px}
.dots i{width:7px;height:7px;border-radius:50%;background:#999;display:block}
.dots i:first-child{background:var(--red)}
.blog .dots{position:absolute;right:14px;top:20px}
.post{display:flex;gap:13px;margin-top:10px}
.post-img{flex:0 0 54px;height:54px;background:linear-gradient(135deg,#5a4a40,#9aa5b0 60%,#2a3a5a)}
.post h4{font-weight:400;font-size:11px;color:#3d5a1a}
.post p{margin-top:4px;font-size:10px;font-weight:300;line-height:15.2px;color:#555}

.quote{top:928px;text-align:center}
.quote blockquote{position:relative;margin-top:12px;font-size:10px;font-style:italic;font-weight:300;line-height:17.2px;color:#555}
.quote .mark{font-family:"Oswald",Arial,sans-serif;font-style:normal;font-weight:500;font-size:40px;color:#555;line-height:0;position:relative;top:16px}
.quote .open{position:absolute;left:0;top:16px}
.quote .close{margin-left:8px}
.quote .name{margin-top:16px;font-size:9.5px;font-style:italic;color:var(--red)}
.quote .place{font-size:9.5px;font-style:italic;color:#888;margin-top:2px}
.quote .dots{justify-content:center;margin-top:22px}

.footer-line{position:absolute;left:98px;top:1105px;width:704px;height:1px;background:#ddd}
.copy{position:absolute;left:98px;top:1129px;font-size:9px;line-height:18px;color:#444}
.copy span{color:var(--red)}
.foot-links{position:absolute;right:98px;top:1129px;font-size:9px;color:#444;line-height:18px}
.foot-links span{margin:0 4px;color:#777}
</style>
</head>
<body>
<div class="brand"><span class="brand-dot"></span>the corvane agency</div>
<div class="top-links">Corporate Site<span>|</span>Our Blog<span>|</span>Site Map</div>
<div class="search"><svg width="18" height="16" viewBox="0 0 18 16"><circle cx="6.5" cy="6.5" r="4.5" fill="none" stroke="#e31b23" stroke-width="2"/><line x1="10" y1="10" x2="16" y2="14.5" stroke="#e31b23" stroke-width="3" stroke-linecap="round"/></svg></div>

<div class="hero" role="img" aria-label="Photo of a smiling couple hugging a tricolour mountain dog outdoors"></div>
<nav class="nav"><a class="active">Home</a><div class="nav-items"><a>Corvane Life</a><a>Our Services</a><a>Pet Experts</a><a>Business Development</a><a>Case Studies</a><a>Our Team</a></div></nav>
<div class="caption">Redefining Pet Industry
  <span class="arrow prev"><svg width="10" height="12"><polyline points="7,2 3,6 7,10" fill="none" stroke="#777" stroke-width="2"/></svg></span>
  <span class="arrow next"><svg width="10" height="12"><polyline points="3,2 7,6 3,10" fill="none" stroke="#777" stroke-width="2"/></svg></span>
</div>

<div class="service svc-pr">Public Relations<div class="thumb" role="img" aria-label="Photo of a woman with a golden retriever and a kitten"></div><span class="foot"></span></div>
<div class="service svc-sm">Social Media<div class="thumb" role="img" aria-label="Photo of a dog looking at a social media page on a screen"></div><span class="foot"></span></div>
<div class="service svc-pc">Product Consulting<div class="thumb" role="img" aria-label="Photo of a consultant presenting a document to a couple"></div><span class="foot"></span></div>

<div class="divider" style="top:588px"></div>
<section class="wrap about">
  <h2 class="section-title">About <em>Corvane</em></h2>
  <p>PR has evolved from public relations to personal relations. As new communication tools have emerged, old habits have been buried, giving way to the consumer revolution of social media. At Corvane, we tap the best ways to connect you with those in the pet industry. That focus makes our team your ideal partner for creating a community as faithful as a favorite pet.</p>
</section>
<div class="divider" style="top:712px"></div>

<div class="card team">
  <h2 class="section-title">Our <em>Team</em></h2>
  <p>The driving force behind our success is the team that makes it happen. Individual skills and experience meet a collective desire to excel in every facet of our work and shape our daily approach to elevate the pet industry through our clients. Each member of our pack provides the strength and stability to run smoothly...</p>
  <div class="more">More</div>
</div>
<div class="card blog">
  <h2 class="section-title">Blog <em>Posts</em></h2>
  <div class="dots"><i></i><i></i><i></i></div>
  <div class="post">
    <div class="post-img" role="img" aria-label="Photo of a pet expert on a television set"></div>
    <div>
      <h4>Trailpaw Featured on Morning Desk</h4>
      <p>Our client Trailpaw was featured with pet expert Dalton Reeve on Morning Desk as part of a holiday pet travel segment. Great job Dalton, but the Auto Hammock and Booster Seat made the segment, if we do say so ourselves.</p>
    </div>
  </div>
</div>

<section class="wrap quote">
  <h2 class="section-title">Client <em>Says..</em></h2>
  <blockquote><span class="mark open">&ldquo;</span>&nbsp;&nbsp;&nbsp;&nbsp;&nbsp;&nbsp;&nbsp;I've had the opportunity to work with Corvane team members and can assure you they are professional, innovative and caring and they are always eager to help. I've worked with them across a wide array of communication campaigns and issues both positive and negative and they have always managed to position the companies I've been with in the most positive manner.<span class="mark close">&rdquo;</span></blockquote>
  <div class="name">Marcus Velden</div>
  <div class="place">Brazil</div>
  <div class="dots"><i></i><i></i><i></i></div>
</section>

<div class="footer-line"></div>
<div class="copy">Copyright © 2014 <span>The Corvane Agency</span><br>All Right Reserved</div>
<div class="foot-links">Contact<span>/</span>Career<span>/</span>Blog<span>/</span>Love List<span>/</span>Site Map</div>
</body>
</html>
```